Wordpress site needed for company's Healthcare Web App

Healthcare web app needs wordpress web design for web site that provides an overview of the product, a page explaining key features, a blog, a press release announcement section, customer testimonials, contact us, sign up page, invite friends.

The website should use the color scheme including in the logo. This web site is not the app, this website will be used to introduce the app.

Target Market(s)

Doctors, enterprise healthcare professionals, patients who will use patient portals to access their health info. (not the app itself, but this site introduces the app)

Industry/Entity Type

Health Care

Coding

Coded - Design and coding required

Number of Pages Required

5+ page

Font styles to use
Sans Serif

Requirements
Must have
• This is a Wordpress based site.
• Product Overview, Key Product Features, Blog, Press Releases, Events, Embedded Videos explaining the product and demo'ing features, Sign Up Page for people interested,
Nice to have
• Uplifting Hero Image for Healthcare Tech, color scheme fitting with logo

```html
<!DOCTYPE html>
<html lang="en">
<head>
<meta charset="utf-8">
<title>CareLedger</title>
<link rel="stylesheet" href="https://fonts.googleapis.com/css2?family=Roboto:wght@400;700;900&family=Lato:wght@400&display=swap">
<style>
  :root {
    --teal: #1f87a4;
    --teal-dark: #166c85;
    --ink: #04161d;
    --navy-btn: #0f3440;
    --white: #ffffff;
    --muted: #a7b3bb;
    --rule: rgba(255,255,255,0.25);
    --scroll: #a9a9a9;
  }
  * { box-sizing: border-box; margin: 0; padding: 0; }
  html, body { width: 1200px; height: 1200px; overflow: hidden; }
  body { position: relative; font-family: "Lato", sans-serif; background: var(--white); }

  .hero { position: absolute; left: 0; top: 0; width: 1200px; height: 429px; background: var(--teal); }
  .site-header { position: absolute; left: 0; top: 0; width: 1200px; height: 64px; border-bottom: 1px solid var(--rule); }
  .brand { position: absolute; left: 188px; top: 14px; display: flex; align-items: center; gap: 10px;
    font-family: "Roboto", sans-serif; font-weight: 700; font-size: 27px; color: var(--white); }
  .brand-mark { width: 34px; height: 34px; border-radius: 50%; background: var(--white); }

  .hero-title { position: absolute; left: 188px; top: 118px; font-family: "Roboto", sans-serif; font-weight: 900;
    font-size: 46px; line-height: 43px; color: var(--white); letter-spacing: 0.5px; }
  .btn { position: absolute; top: 322px; height: 40px; border-radius: 22px; font-family: "Roboto", sans-serif;
    font-weight: 700; font-size: 20px; display: flex; align-items: center; justify-content: center; letter-spacing: 0.5px; }
  .btn-signup { left: 170px; width: 168px; background: var(--white); color: var(--teal); }
  .btn-more { left: 347px; width: 196px; border: 3px solid var(--white); color: var(--white); }

  .slider-arrow { position: absolute; top: 200px; width: 28px; height: 28px; border-radius: 50%; background: var(--navy-btn); }
  .slider-arrow svg { display: block; }
  .slider-prev { left: 14px; }
  .slider-next { left: 1157px; }

  .devices-visual { position: absolute; left: 571px; top: 124px; width: 571px; height: 240px; border-radius: 6px;
    background: linear-gradient(135deg, #e9eef1 0%, #c9d3d8 55%, #8fa3ab 100%); opacity: 0.9; }

  .overview { position: absolute; left: 0; top: 429px; width: 1200px; height: 468px; background: var(--white); }
  .overview-title { position: absolute; left: 181px; top: 57px; font-family: "Roboto", sans-serif; font-weight: 900;
    font-size: 55px; line-height: 60px; color: var(--teal); }
  .overview-text { position: absolute; left: 182px; top: 122px; width: 412px; font-size: 11.3px; line-height: 17.3px; color: var(--muted); }
  .overview-visual { position: absolute; left: 630px; top: 127px; width: 380px; height: 220px;
    background: linear-gradient(135deg, #2b3440 0%, #8a9fb0 40%, #dfe7ee 70%, #3fb7e6 100%); border-radius: 4px; }
  .to-top { position: absolute; left: 1158px; top: 131px; width: 20px; height: 20px; background: var(--scroll); border-radius: 2px; }

  .features { position: absolute; left: 0; top: 897px; width: 1200px; height: 303px; background: var(--ink); overflow: hidden; }
  .features-visual { position: absolute; left: 110px; top: 141px; width: 352px; height: 180px; border-radius: 10px 10px 0 0;
    background: linear-gradient(135deg, var(--teal) 0%, #2a9ab8 60%, #5ab5cc 100%); border: 10px solid #1b1f22; border-bottom: none; }
  .features-icon { position: absolute; left: 659px; top: 137px; }
  .features-title { position: absolute; left: 750px; top: 131px; font-family: "Roboto", sans-serif; font-weight: 900;
    font-size: 32px; line-height: 36px; color: var(--white); }
  .features-text { position: absolute; left: 600px; top: 198px; width: 500px; font-size: 11.2px; line-height: 17.2px; color: var(--white); }
</style>
</head>
<body>
  <section class="hero">
    <header class="site-header">
      <div class="brand"><span class="brand-mark"></span>CareLedger</div>
    </header>
    <h1 class="hero-title">GET ACCESS<br>ANYTIME<br>ANYWHERE</h1>
    <a class="btn btn-signup">SIGN ME UP</a>
    <a class="btn btn-more">TELL ME MORE</a>
    <div class="slider-arrow slider-prev">
      <svg width="28" height="28" viewBox="0 0 28 28"><path d="M16 9 L11 14 L16 19" fill="none" stroke="#fff" stroke-width="2.6"/></svg>
    </div>
    <div class="slider-arrow slider-next">
      <svg width="28" height="28" viewBox="0 0 28 28"><path d="M12 9 L17 14 L12 19" fill="none" stroke="#fff" stroke-width="2.6"/></svg>
    </div>
    <div class="devices-visual" role="img" aria-label="Desktop, laptop, tablet and phone showing the web app"></div>
  </section>

  <section class="overview">
    <h2 class="overview-title">PRODUCT OVERVIEW</h2>
    <p class="overview-text">Lorem ipsum dolor sit amet, consectetur adipiscing elit. Sed consequat lacinia lacus vitae sagittis. Vivamus eu ultrices velit, bibendum vestibulum lorem. Donec id nisi gravida massa finibus cursus. Mauris euismod, nulla non sagittis maximus, tellus elit lobortis nibh, nec rutrum ex libero non massa. Curabitur tempor, justo ut pellentesque congue, magna felis faucibus nisl, id vulputate lectus odio vel ante. Aliquam magna nisl, consequat at tortor scelerisque, fringilla rhoncus velit. Curabitur lobortis hendrerit nunc non mollis. Aliquam lacus orci, iaculis at ipsum ac, elementum finibus lacus. Cum sociis natoque penatibus et magnis dis parturient montes, nascetur ridiculus mus. Donec sollicitudin sem eu enim mollis rhoncus. Donec ornare aliquet tellus in aliquam. Proin lobortis augue lorem, vel pellentesque augue iaculis non.</p>
    <div class="overview-visual" role="img" aria-label="Web page preview of the app with article photos"></div>
    <div class="to-top">
      <svg width="20" height="20" viewBox="0 0 20 20"><path d="M7 11.5 L10 8.5 L13 11.5" fill="none" stroke="#fff" stroke-width="1.4"/></svg>
    </div>
  </section>

  <section class="features">
    <div class="features-visual" role="img" aria-label="Laptop screen showing the app welcome screen"></div>
    <svg class="features-icon" width="30" height="30" viewBox="0 0 30 30">
      <circle cx="15" cy="15" r="15" fill="#fff"/>
      <rect x="12.8" y="6" width="4.4" height="12" rx="1.5" fill="#04161d"/>
      <circle cx="15" cy="22.5" r="2.4" fill="#04161d"/>
    </svg>
    <h2 class="features-title">AMAZING FEATURES</h2>
    <p class="features-text">Lorem ipsum dolor sit amet, consectetur adipiscing elit. Sed consequat lacinia lacus vitae sagittis. Vivamus eu ultrices velit, bibendum vestibulum lorem. Donec id nisi gravida massa finibus cursus. Mauris euismod, nulla non sagittis maximus, tellus elit lobortis nibh, nec rutrum ex libero non massa. Curabitur tempor, justo ut pellentesque congue, magna felis faucibus nisl, id vulputate lectus odio vel ante. Aliquam magna nisl, consequat at tortor scelerisque, fringilla rhoncus velit. Curabitur lobortis hendrerit nunc non mollis. Aliquam lacus orci, iaculis at ipsum ac, elementum finibus lacus. Cum sociis natoque penatibus et magnis dis parturient montes, nascetur ridiculus mus.</p>
  </section>
</body>
</html>
```